Brand and Marketing Coach Needs PDF Designed

I have content that i need placed into a simple but great PDF design. The PDF is about the formula I use to build personal brands. This is geared towards entrepreneurs, experts, coaches, therapists, wellness practitioners, and indpendent business owners who serve to improve the lives of others.
The company name is changing from Corvelta Studio to Growth with Neighbors (I don't have that logo yet, so working backwards a bit. For now, the Corvelta Studio logo can be used.) My brand is NOT formal and corporate, but it's also not neon-pink and screaming at you. It's down to earth, hip, a bit modern but warm. It's about no BS and authenticity. The final deliverable should make the reader feel focused, smart, motivated and hopeful.

Target Market(s)

Conscious entrepreneurs and small business owners. this one is specifically for pharmacy entrepreneurs but this will be used for various audiences later.

Font styles to use
Sans Serif

Colors
eaf1f7
3377b5
6b449b
f37122
faa54b
f68e4e
ffc214

Requirements
Must have
• Modern design. colors that match logo - 4e5583 (i think that is the blue.) d65a40.
• Could have these colors as well: c6a254, 01bcc3
• But open to other colors
Nice to have
• I'd like to see some ways to make this PDF simple and readable, and eye-catching. I'd also like to use the uploaded ebooks for design ideas.
Should not have
• neon colors, clip art

```html
<!DOCTYPE html>
<html lang="en">
<head>
<meta charset="utf-8">
<title>The Personal Brand Formula — Cover</title>
<link rel="stylesheet" href="https://fonts.googleapis.com/css2?family=Montserrat:wght@300;400;600;700&display=swap">
<style>
  :root {
    --backdrop: #e4e4e2;
    --page: #eef1f4;
    --spine-blue: #3377b5;
    --band-orange: #e8692a;
    --title-purple: #6b449b;
    --body-grey: #4a4a4f;
    --rule-grey: #b9bcc4;
  }
  * { margin: 0; padding: 0; box-sizing: border-box; }
  html, body {
    width: 1200px;
    height: 699px;
    overflow: hidden;
    background: var(--backdrop);
    font-family: "Montserrat", sans-serif;
  }
  .canvas {
    width: 1200px;
    height: 699px;
    display: flex;
    align-items: center;
    justify-content: center;
  }
  .cover {
    position: relative;
    width: 960px;
    height: 660px;
    background: var(--page);
    overflow: hidden;
    box-shadow: 0 6px 24px rgba(0, 0, 0, 0.12);
  }
  .cover__spine {
    position: absolute;
    left: 0;
    top: 0;
    width: 22px;
    height: 100%;
    background: var(--spine-blue);
  }
  .publisher {
    position: absolute;
    top: 40px;
    right: 40px;
    display: flex;
    align-items: center;
    gap: 12px;
    color: var(--body-grey);
    white-space: nowrap;
  }
  .publisher__tagline {
    font-size: 11px;
    font-weight: 400;
    letter-spacing: 1px;
    text-transform: uppercase;
    padding-right: 12px;
    border-right: 1px solid var(--rule-grey);
  }
  .publisher__name {
    font-size: 18px;
    font-weight: 400;
    letter-spacing: 0.5px;
  }
  .title {
    position: absolute;
    left: 22px;
    top: 210px;
  }
  .title__lead {
    margin-left: 100px;
    font-size: 58px;
    font-weight: 300;
    line-height: 1;
    color: var(--title-purple);
    letter-spacing: 1px;
  }
  .title__band {
    display: inline-block;
    background: var(--band-orange);
    color: #fff;
    line-height: 1;
    padding: 8px 26px 8px 100px;
  }
  .title__band--main {
    margin-top: 6px;
    font-size: 60px;
    font-weight: 300;
    letter-spacing: 1px;
  }
  .title__band--formula {
    display: block;
    width: fit-content;
    margin-top: 4px;
    font-size: 62px;
    font-weight: 700;
    letter-spacing: 2px;
  }
  .title__audience {
    margin: 22px 0 0 100px;
    font-size: 29px;
    font-weight: 600;
    color: var(--title-purple);
  }
  .title__summary {
    margin: 14px 0 0 100px;
    font-size: 22px;
    font-weight: 400;
    line-height: 1.3;
    color: var(--body-grey);
  }
</style>
</head>
<body>
  <main class="canvas">
    <section class="cover">
      <div class="cover__spine"></div>

      <div class="publisher">
        <span class="publisher__tagline">Growth with Neighbors</span>
        <span class="publisher__name">Corvelta Studio</span>
      </div>

      <div class="title">
        <h1>
          <div class="title__lead">THE</div>
          <span class="title__band title__band--main">PERSONAL BRAND</span>
          <span class="title__band title__band--formula">FORMULA</span>
        </h1>
        <p class="title__audience">For Pharmacy Entrepreneurs</p>
        <p class="title__summary">The quick n’ dirty guide to creating a unique<br>personal brand that attracts your ideal clients.</p>
      </div>
    </section>
  </main>
</body>
</html>
```